Luxury WordPress Website for CORALBASINS

I need a professional WordPress website for Coral Basins. The site should be modern, visually appealing, and user-friendly, reflecting the brand’s luxury and premium identity. It must include a homepage, product/service pages, contact form, and be responsive on both desktop and mobile devices. The design should allow for easy updates and integration of future content, while maintaining a polished and professional look.

Target Market(s)

swimmingpool & spa

Industry/Entity Type

Swimmingpool

Coding

Coded - Design and coding required

Font styles to use
Other font styles liked:
• HaboroSoft

Requirements
Must have
• Exclusive appearance
Nice to have
• • A logo that subtly incorporates water or pool elements. • A color palette that reflects luxury, elegance, and relaxation. • Clean and modern typography that is easy to read across all media. • Iconography or design elements that convey premium quality. • A versatile design that can be adapted for social media, merchandise, and promotional materials. • Optional: A tagline that emphasizes luxury and high-end pool experiences.

```html
<!DOCTYPE html>
<html lang="en">
<head>
<meta charset="utf-8">
<title>Coral Basins</title>
<link href="https://fonts.googleapis.com/css2?family=Roboto:wght@400;500;700&display=swap" rel="stylesheet">
<style>
:root{
  --teal:#2fbf9a;
  --ink:#111111;
  --muted:#888888;
  --paper:#f1f1f1;
  --white:#ffffff;
}
*{margin:0;padding:0;box-sizing:border-box}
html,body{width:719px;height:1200px;overflow:hidden}
body{font-family:"Roboto",Arial,sans-serif;color:var(--ink);background:var(--white)}
.site-header{height:39px;display:flex;align-items:center;padding-left:9px;gap:6px}
.brand-dot{width:11px;height:11px;border-radius:50%;background:var(--teal)}
.brand-name{font-size:12px;font-weight:400;color:var(--ink)}
.hero{height:302px;position:relative;display:flex;flex-direction:column;align-items:center;
  background:radial-gradient(ellipse at 60% 30%,#7a5a45 0%,#4b3a30 45%,#2a2624 100%)}
.hero-title{margin-top:106px;font-size:30px;font-weight:700;color:var(--white);line-height:36px;letter-spacing:-.3px}
.hero-sub{margin-top:6px;font-size:9.5px;color:var(--white);line-height:12px}
.btn{display:inline-flex;align-items:center;justify-content:center;height:26px;width:102px;border-radius:13px;font-size:9px;text-decoration:none}
.btn-primary{margin-top:13px;background:var(--teal);color:var(--white)}
.btn-light{background:var(--white);color:var(--teal)}
main{background:var(--paper);height:681px}
.section-title{font-size:18px;font-weight:700;text-align:center;line-height:22px}
.about{height:219px;padding-top:31px}
.about-lead{text-align:center;font-size:10px;line-height:14px;margin-top:6px}
.services{display:grid;grid-template-columns:225px 226px 225px;gap:12px;margin:32px 10px 0 9px}
.service-card{background:var(--white);border-radius:6px;height:93px;padding:12px 12px}
.service-card svg{width:22px;height:22px;display:block}
.service-card h3{font-size:12px;font-weight:700;line-height:15px;margin-top:8px}
.service-card p{font-size:7.5px;line-height:9.5px;margin-top:3px}
.showcase{height:208px;padding-top:11px}
.gallery{display:grid;grid-template-columns:201px 201px 225px;column-gap:37px;margin:15px 10px 0 9px}
.gallery-item{height:150px;border-radius:10px}
.g1{background:linear-gradient(160deg,#c9c7c0 0%,#8aa39e 45%,#2b8f93 100%)}
.g2{background:linear-gradient(170deg,#3f7fa8 0%,#b9c2b4 40%,#e6e2db 70%,#7fc6c8 100%)}
.g3{background:linear-gradient(180deg,#b7aa98 0%,#7d7566 40%,#3b9fc6 75%,#4a3f36 100%)}
.why{height:112px;padding-top:19px}
.reasons{display:grid;grid-template-columns:180px 160px 184px 176px;margin-top:19px}
.reason{text-align:center}
.reason svg{width:19px;height:19px;display:block;margin:0 auto}
.reason span{display:block;font-size:10px;line-height:12px;margin-top:5px}
.testimonials{height:142px;padding-top:16px}
.quotes{display:grid;grid-template-columns:354px 332px;column-gap:14px;margin:16px 10px 0 9px}
.quote{background:var(--white);border-radius:6px;height:56px;padding:13px 18px}
.quote p{font-size:7.5px;line-height:10px}
.quote cite{display:block;font-style:normal;font-size:7.5px;color:var(--muted);margin-top:9px}
.cta{height:122px;background:var(--teal);display:flex;flex-direction:column;align-items:center;padding-top:31px}
.cta h2{color:var(--white);font-size:18px;line-height:22px;font-weight:700}
.cta .btn{margin-top:11px}
.site-footer{height:56px;text-align:center;padding-top:15px}
.social{display:flex;justify-content:center;gap:13px}
.social span{width:10px;height:10px;border-radius:50%;background:var(--ink)}
.copyright{font-size:7.5px;margin-top:13px}
</style>
</head>
<body>
<header class="site-header">
  <span class="brand-dot"></span>
  <span class="brand-name">Coral Basins</span>
</header>

<section class="hero" role="img" aria-label="Infinity pool at sunset overlooking the sea beside a covered terrace">
  <h1 class="hero-title">Experience Luxury Like Never Before</h1>
  <p class="hero-sub">Creating Dreams with Water</p>
  <a class="btn btn-primary" href="#showcase">Explore Our Pools</a>
</section>

<main>
  <section class="about">
    <h2 class="section-title">About Coral Basins</h2>
    <p class="about-lead">At Coral Basins, we blend luxury and precision to craft the most exquisite swimming experiences.</p>
    <div class="services">
      <article class="service-card">
        <svg viewBox="0 0 24 24" fill="none" stroke="#2fbf9a" stroke-width="2" stroke-linecap="round"><path d="M7 18V7a3 3 0 0 1 5-2M15 18V7a3 3 0 0 1 5-2M7 10h8M7 14h8"/><path d="M2 20q2.5-2 5 0t5 0 5 0 5 0"/></svg>
        <h3>Custom Pools</h3>
        <p>Tailored to perfection with the finest materials and bespoke designs.</p>
      </article>
      <article class="service-card">
        <svg viewBox="0 0 24 24" fill="none" stroke="#2fbf9a" stroke-width="2.4"><path d="M12 12c-2-3-4-4-6-4a4 4 0 0 0 0 8c2 0 4-1 6-4s4-4 6-4a4 4 0 0 1 0 8c-2 0-4-1-6-4z"/></svg>
        <h3>Infinity Pools</h3>
        <p>Seamlessly blending into the horizon, offering breathtaking views.</p>
      </article>
      <article class="service-card">
        <svg viewBox="0 0 24 24" fill="#2fbf9a"><path d="M12 4c2 2 3 4 3 7s-1 5-3 6c-2-1-3-3-3-6s1-5 3-7z"/><path d="M2 10c4 0 8 2 10 8-6 1-10-2-10-8zM22 10c-4 0-8 2-10 8 6 1 10-2 10-8z"/></svg>
        <h3>Spa &amp; Jacuzzi</h3>
        <p>Relax in style with our luxurious spa and jacuzzi installations.</p>
      </article>
    </div>
  </section>

  <section class="showcase" id="showcase">
    <h2 class="section-title">Luxury Showcase</h2>
    <div class="gallery">
      <div class="gallery-item g1" role="img" aria-label="Modern villa pool beside a rock wall with sun loungers"></div>
      <div class="gallery-item g2" role="img" aria-label="Resort pool lined with white sun loungers under palm trees"></div>
      <div class="gallery-item g3" role="img" aria-label="Rooftop infinity pool overlooking a city skyline"></div>
    </div>
  </section>

  <section class="why">
    <h2 class="section-title">Why Choose Us</h2>
    <div class="reasons">
      <div class="reason">
        <svg viewBox="0 0 24 24" fill="#2fbf9a"><path d="M6 3h12l5 6-11 13L1 9z"/></svg>
        <span>Craftsmanship</span>
      </div>
      <div class="reason">
        <svg viewBox="0 0 24 24" fill="#2fbf9a"><rect x="8" y="2" width="8" height="8" rx="1"/><rect x="3" y="12" width="8" height="8" rx="1"/><rect x="13" y="12" width="8" height="8" rx="1"/></svg>
        <span>Premium Materials</span>
      </div>
      <div class="reason">
        <svg viewBox="0 0 24 24" fill="#2fbf9a"><path d="M17 2l5 5L8 21H3v-5z"/><rect x="2" y="3" width="6" height="6" transform="rotate(45 5 6)"/><rect x="16" y="15" width="6" height="6" transform="rotate(45 19 18)"/></svg>
        <span>Bespoke Design</span>
      </div>
      <div class="reason">
        <svg viewBox="0 0 24 24" fill="#2fbf9a"><path d="M12 2l3 7 7 .6-5.3 4.6L18.4 22 12 18l-6.4 4 1.7-7.8L2 9.6 9 9z"/></svg>
        <span>Guaranteed Perfection</span>
      </div>
    </div>
  </section>

  <section class="testimonials">
    <h2 class="section-title">Testimonials</h2>
    <div class="quotes">
      <blockquote class="quote">
        <p>"Coral Basins transformed our backyard into a paradise. The craftsmanship is unrivaled!"</p>
        <cite>- Clara M.</cite>
      </blockquote>
      <blockquote class="quote">
        <p>"Their bespoke design exceeded our expectations. Truly elegant &amp; luxurious!"</p>
        <cite>- Daniel R.</cite>
      </blockquote>
    </div>
  </section>
</main>

<section class="cta">
  <h2>Ready to Dive into Luxury?</h2>
  <a class="btn btn-light" href="#contact">Contact Us Today</a>
</section>

<footer class="site-footer" id="contact">
  <div class="social">
    <span aria-label="Social link"></span>
    <span aria-label="Social link"></span>
    <span aria-label="Social link"></span>
  </div>
  <p class="copyright">© 2023 Coral Basins. All rights reserved.</p>
</footer>
</body>
</html>
```